Tennis String Package

Need a design for a tennis string package.
Design to be 15 cm in length and width.
I would like to create a style like the one in the image.
Brand name VUMIK
Product name SANDPIPER
Front and back designs are required.

Colors
0054AA
0677BA
7BADD7
CADEEF
E8F1F8
A7469A
B969AE
D3A5CF
EDDBEB
F8F0F9
6B429C
8869AF
B7A5CE
E3DAEB
F3F0F8

```html
<!DOCTYPE html>
<html lang="en">
<head>
<meta charset="utf-8">
<title>VUMIK Sandpiper – Tennis String Package</title>
<link rel="stylesheet" href="https://fonts.googleapis.com/css2?family=Nunito+Sans:wght@300;400&display=swap">
<style>
  :root {
    --backdrop: #ebeceb;
    --package-blue: #5b6f8b;
    --label-white: #ffffff;
    --shadow: rgba(0, 0, 0, 0.22);
  }
  html, body {
    margin: 0;
    padding: 0;
    width: 1200px;
    height: 1200px;
    overflow: hidden;
    background: var(--backdrop);
  }
  .canvas {
    position: relative;
    width: 1200px;
    height: 1200px;
  }
  .package-front {
    position: absolute;
    left: 222px;
    top: 222px;
    width: 756px;
    height: 756px;
    background: var(--package-blue);
    box-shadow: 6px 8px 8px var(--shadow);
  }
  .package-type {
    position: absolute;
    inset: 0;
    width: 756px;
    height: 756px;
    font-family: "Nunito Sans", "Avenir Next", sans-serif;
    fill: var(--label-white);
  }
  .brand-name { font-size: 84px; font-weight: 300; }
  .product-name { font-size: 41px; font-weight: 300; }
  .product-category { font-size: 36px; font-weight: 300; letter-spacing: 0.5px; }
</style>
</head>
<body>
  <main class="canvas">
    <section class="package-front">
      <svg class="package-type" viewBox="0 0 756 756" xmlns="http://www.w3.org/2000/svg">
        <text class="brand-name" x="96" y="408">VUMIK</text>
        <text class="product-name" x="488" y="375">SANDPIPER</text>
        <text class="product-category" x="378" y="664" text-anchor="middle">Tennis String</text>
      </svg>
    </section>
  </main>
</body>
</html>
```